Business Card Design Project

Same as the logo requirements.
Address of the store is:
Milo's Waypost, LLC
287B North Ferncliff Ave Suite 4
Maplecrest, IN 46592
Gerald Pinkney, Owner

Reason: The design of the business cards should be the same as the main logo.

Reason: I approved the wrong design!

This is the link to the current logo design: http://files.pixelbazaar-example.net/img/720415/391826/391826_5092741_720415_image.jpg

Target Market(s)

Courthouse and downtown employees, including lawyers, judges, downtown office workers.

Industry/Entity Type

Store

Font styles to use
Serif

Requirements
Must have
• Milo's Waypost
A Convenience Store, and More, on Lindenfield Plaza!
Maplecrest, IN 46592
Nice to have
• Colorful, Arrow sign

```html
<!DOCTYPE html>
<html lang="en">
<head>
<meta charset="utf-8">
<title>Milo's Waypost, LLC — Business Card</title>
<link rel="stylesheet" href="https://fonts.googleapis.com/css2?family=Marcellus&family=Marcellus+SC&display=swap">
<style>
  :root {
    --page-bg: #e9e6e0;
    --card-bg: #6cc7d0;
    --card-shade: #5fb9c3;
    --ink: #2f3a7a;
    --mark: #3a4585;
  }
  html, body {
    margin: 0;
    padding: 0;
    width: 1200px;
    height: 800px;
    overflow: hidden;
    background: var(--page-bg);
  }
  .canvas {
    width: 1200px;
    height: 800px;
    display: flex;
    align-items: center;
    justify-content: center;
  }
  .business-card {
    width: 1000px;
    height: 572px;
    background: linear-gradient(135deg, var(--card-bg) 0%, var(--card-shade) 100%);
    box-shadow: 0 10px 30px rgba(0, 0, 0, 0.18);
    display: flex;
    flex-direction: column;
    align-items: center;
    justify-content: center;
    text-align: center;
    color: var(--ink);
    box-sizing: border-box;
    padding-top: 10px;
  }
  .brand {
    display: flex;
    flex-direction: column;
    align-items: center;
  }
  .brand-dot {
    width: 34px;
    height: 34px;
    background: var(--mark);
    margin-bottom: 14px;
  }
  .brand-name {
    font-family: "Marcellus SC", serif;
    font-size: 42px;
    letter-spacing: 1px;
    margin: 0;
    font-weight: 400;
  }
  .person {
    margin-top: 52px;
  }
  .person-name {
    font-family: "Marcellus SC", serif;
    font-size: 38px;
    letter-spacing: 1px;
    margin: 0;
    line-height: 1;
  }
  .person-role {
    font-family: "Marcellus", serif;
    font-size: 21px;
    letter-spacing: 1.5px;
    margin: 2px 0 0;
  }
  .contact {
    font-family: "Marcellus", serif;
    font-size: 27px;
    letter-spacing: 1.5px;
    line-height: 1.2;
  }
  .contact-phone {
    margin: 36px 0 0;
  }
  .contact-address {
    margin: 30px 0 0;
    font-style: normal;
  }
</style>
</head>
<body>
  <main class="canvas">
    <article class="business-card">
      <header class="brand">
        <div class="brand-dot" aria-hidden="true"></div>
        <h1 class="brand-name">Milo's Waypost, LLC</h1>
      </header>
      <section class="person">
        <p class="person-name">Gerald Pinkney</p>
        <p class="person-role">Owner</p>
      </section>
      <p class="contact contact-phone">+1 (330) 5550 172</p>
      <address class="contact contact-address">
        287B North Ferncliff Ave Suite 4<br>
        Maplecrest, IN 46592
      </address>
    </article>
  </main>
</body>
</html>
```